Stainless Steel Water Bottle Packaging

We need a design for our cylindrical water bottle packaging.

Please see attached template (500ml cola bottle template .ai file) for exact dimensions.

VORO is defined as the elemental forces of nature embodied in an object or person. The design should be eye catching and draw potential clients in. Although its a cylindrical bottle/box, the front which would face the customer when sitting on a shelf should clearly display our logo.

Industry/Entity Type

Steel

Requirements
Must have
• Designed to the specifications of the attached template (see attached)
• Our VORO Logo (see attached) and website www.vorobottle.example(in smaller font) must appear.
• Size of bottle must appear - '17 oz/500 ml'
• These should appear somewhere:
• 'INULATED DOUBLE-WALL STAINLESS STEEL WATER BOTTLE'
• 'VORO Bottles magically keeps drinks cold for up to 24hrs, hot for 12',
• 'BPA Free'
• 'For every VORO bottle purchased, a portion of proceeds will go towards charity. Each of our colour's have been assigned a specific charity. Please visit www.vorobottle.example to find out which charity you helped support!'
• The Top circle - just our Symbol (flame/drop)
• The bottom circle - 'Inc. Designed in Canada made in China' on the outer edge leaving the middle empty for the UPC code.
• Reference website for the bottle case I'm looking for:
• http://shopkorinday.example/t-flow-lagoon-pink-insulated-water-bottle
Nice to have
• illustration of our water bottle shape (see attached) appearing somewhere on the box is something i had in mind but definitely not necessary.

```html
<!DOCTYPE html>
<html lang="en">
<head>
<meta charset="utf-8">
<title>VORO Bottle Packaging</title>
<link rel="stylesheet" href="https://fonts.googleapis.com/css2?family=Oswald:wght@400;500;600&family=Roboto+Condensed:wght@400&display=swap">
<style>
  :root {
    --stage: #d9dadc;
    --tube-blue: #2a9fd6;
    --tube-blue-light: #3db0e2;
    --band-white: #f0f0ee;
    --panel-teal: #1f6f93;
    --logo-blue: #2b9ad2;
    --text-light: #d6eef8;
    --white: #ffffff;
  }
  html, body {
    margin: 0;
    padding: 0;
    width: 1200px;
    height: 1200px;
    overflow: hidden;
    background: var(--stage);
  }
  .canvas {
    position: relative;
    width: 1200px;
    height: 1200px;
  }
  .tube {
    position: absolute;
    top: 140px;
    width: 340px;
    height: 930px;
    border-radius: 6px;
    overflow: hidden;
    background: var(--tube-blue);
  }
  .tube--back { left: 190px; }
  .tube--front { left: 670px; }
  .wave-area {
    position: absolute;
    left: 0;
    width: 100%;
    background: linear-gradient(180deg, var(--tube-blue-light), var(--tube-blue));
  }
  .wave-area--top { top: 0; height: 200px; }
  .wave-area--bottom { top: 440px; height: 490px; }
  .cap-line {
    position: absolute;
    top: 36px;
    left: 0;
    width: 100%;
    height: 2px;
    background: rgba(0, 0, 0, 0.12);
  }
  .band {
    position: absolute;
    top: 200px;
    left: 0;
    width: 100%;
    height: 240px;
    background: var(--band-white);
  }
  .illustration-area {
    position: absolute;
    top: 205px;
    left: 75px;
    width: 190px;
    height: 690px;
    border-radius: 24px;
    background: var(--panel-teal);
  }
  .bottle-copy {
    position: absolute;
    top: 330px;
    left: 87px;
    width: 166px;
    display: flex;
    flex-direction: column;
    align-items: center;
    text-align: center;
    color: var(--text-light);
    font-family: 'Oswald', sans-serif;
  }
  .bottle-copy__title {
    font-weight: 600;
    font-size: 17px;
    line-height: 1.2;
    letter-spacing: 0.5px;
    margin: 0 0 34px;
  }
  .brand-name {
    display: flex;
    align-items: center;
    gap: 8px;
    font-family: 'Oswald', sans-serif;
    font-weight: 500;
    color: var(--logo-blue);
    letter-spacing: 3px;
  }
  .brand-name__dot {
    border-radius: 50%;
    background: var(--logo-blue);
  }
  .bottle-copy .brand-name { font-size: 34px; margin-bottom: 28px; }
  .bottle-copy .brand-name__dot { width: 10px; height: 10px; }
  .bottle-copy__claim {
    font-size: 14px;
    line-height: 1.35;
    margin: 0 0 28px;
  }
  .bottle-copy__claim span { display: block; }
  .bottle-copy__charity {
    font-family: 'Roboto Condensed', sans-serif;
    font-size: 9.5px;
    line-height: 1.35;
    text-align: left;
    margin: 0 0 26px;
  }
  .bottle-copy__bpa {
    display: flex;
    align-items: center;
    gap: 4px;
    font-family: 'Roboto Condensed', sans-serif;
    font-size: 13px;
    color: var(--text-light);
  }
  .bpa-mark {
    width: 12px;
    height: 12px;
    border-radius: 50%;
    background: var(--text-light);
  }
  .tube--front .brand-name {
    position: absolute;
    top: 200px;
    left: 0;
    width: 100%;
    height: 240px;
    justify-content: center;
    font-size: 60px;
  }
  .tube--front .brand-name__dot { width: 16px; height: 16px; }
  .size-label {
    position: absolute;
    bottom: 40px;
    left: 0;
    width: 100%;
    margin: 0;
    text-align: center;
    font-family: 'Oswald', sans-serif;
    font-weight: 500;
    font-size: 20px;
    color: var(--white);
    letter-spacing: 0.5px;
  }
</style>
</head>
<body>
<main class="canvas">

  <section class="tube tube--back" aria-label="Back panel">
    <div class="wave-area wave-area--top" role="img" aria-label="Wavy water line pattern"></div>
    <div class="cap-line"></div>
    <div class="band"></div>
    <div class="wave-area wave-area--bottom" role="img" aria-label="Wavy water line pattern"></div>

    <div class="illustration-area" role="img" aria-label="Illustration of the water bottle shape"></div>

    <div class="bottle-copy">
      <p class="bottle-copy__title">INULATED<br>DOUBLE-WALL<br>STAINLESS STEEL<br>WATER BOTTLE</p>
      <div class="brand-name"><span class="brand-name__dot"></span>VORO</div>
      <p class="bottle-copy__claim">VORO Bottles<br>magically keeps drinks:<span>• Cold for up to 24hrs</span><span>• Hot for 12hrs</span></p>
      <p class="bottle-copy__charity">For every VORO bottle purchased, a portion of proceeds will go towards charity. Each of our colour's have been assigned a specific charity. Please visit www.vorobottle.example to find out which charity you helped support!</p>
      <div class="bottle-copy__bpa"><span class="bpa-mark"></span>BPA Free</div>
    </div>
  </section>

  <section class="tube tube--front" aria-label="Front panel">
    <div class="wave-area wave-area--top" role="img" aria-label="Wavy water line pattern"></div>
    <div class="cap-line"></div>
    <div class="band"></div>
    <div class="brand-name"><span class="brand-name__dot"></span>VORO</div>
    <div class="wave-area wave-area--bottom" role="img" aria-label="Wavy water line pattern"></div>
    <p class="size-label">17oz/500ml</p>
  </section>

</main>
</body>
</html>
```